Business Card Design Project

We require a business card template to cover basic contact information - our company logo, names of employees, title, mobile and email.

Target Market(s)

Corporate

Industry/Entity Type

Business

Font styles to use
Sans Serif

Requirements
Nice to have
• Thinking it would be great just to have the logo taking up approximately half the space (so it goes as far across the top of the card as possible) and then contact details in the lower half of the card. Keen just to use only the two colours in the logo, on a white background.
Should not have
• No fussy drawings

```html
<!DOCTYPE html>
<html lang="en">
<head>
<meta charset="utf-8">
<title>Tidewell developments – business card</title>
<link href="https://fonts.googleapis.com/css2?family=PT+Sans:wght@400;700&display=swap" rel="stylesheet">
<style>
  :root {
    --teal: #36bfcb;
    --teal-soft: #7fd6de;
    --navy: #2d5fa6;
    --paper: #ffffff;
    --backdrop: #e9edf0;
  }
  html, body {
    margin: 0;
    width: 1200px;
    height: 576px;
    overflow: hidden;
    background: var(--backdrop);
    font-family: "PT Sans", sans-serif;
  }
  .card {
    position: absolute;
    left: 150px;
    top: 31px;
    width: 900px;
    height: 514px;
    background: var(--paper);
    box-shadow: 0 6px 24px rgba(0,0,0,0.12);
  }
  .brand {
    position: absolute;
    left: 60px;
    right: 60px;
    top: 70px;
    margin: 0;
    text-align: center;
    color: var(--teal);
    font-weight: 400;
    font-size: 72px;
    line-height: 1.1;
    white-space: nowrap;
  }
  .name-band {
    position: absolute;
    left: 200px;
    top: 245px;
    width: 480px;
    height: 66px;
    background: linear-gradient(90deg, var(--teal-soft), var(--teal));
  }
  .name {
    position: absolute;
    left: 200px;
    top: 245px;
    width: 480px;
    margin: 0;
    text-align: center;
    color: var(--paper);
    font-weight: 700;
    font-size: 34px;
    line-height: 66px;
  }
  .contact {
    position: absolute;
    color: var(--teal);
    font-size: 30px;
    line-height: 1.25;
  }
  .contact p { margin: 0; }
  .contact-direct { left: 60px; top: 335px; }
  .contact-office { left: 470px; top: 405px; }
</style>
</head>
<body>
  <main class="card">
    <h1 class="brand">Tidewell developments</h1>

    <div class="name-band" role="img" aria-label="Ribbon banner behind the employee name"></div>
    <p class="name">Lena Hartwell</p>

    <div class="contact contact-direct">
      <p>+70 555018264</p>
      <p>hello@tidewell.com</p>
    </div>
    <div class="contact contact-office">
      <p>www.tidewell.com</p>
      <p>Harbourton, 58 Coastline Rd</p>
    </div>
  </main>
</body>
</html>
```